High-End Print/Digital Ad for Unique Luxury Travel Company Required

Objective:
Design a compelling and visually striking advertisement that highlights our company’s unmatched luxury travel experiences. The ad should elevate our brand image, spark curiosity, and drive prospective clients to contact us.
Target Audience:
• Affluent individuals seeking extraordinary, tailor-made travel experiences
• Affluent, luxury, high-net-worth individuals looking for value, expertise, and white-glove service
• Professionals or retirees who appreciate unique, thoughtfully curated travel over mainstream tourism
Key Messages to Communicate:
• One-of-a-kind luxury travel: Once-in-a-lifetime experiences that are curated with creativity and meticulous attention to detail
• Exceptional service: White-glove, personalized planning from start to finish
• 38 years’ travel experience – expert knowledge of destinations, modes of travel, premium accommodations and well-established, meaningful industry connections.
• Highly trusted: Cruise line executives often say, “No one does what you do.”
Tone and Style:
• Elegant, luxurious, sophisticated
• Eye-catching, polished, and modern
• Professional but warm—conveys trust and credibility
• High-impact visuals (full-bleed imagery, custom graphics, or high-end photography)
Deliverables:
• One full-page print ad and digital ad
• Ready-to-print, high-resolution file + working file (PSD, AI, etc.)
Optional: Social media-optimized version or short motion-graphic variation (if designer offers it)
Inspiration & Visual Style Suggestions:
• Think Velvet Voyager, Brimley Hart Wanderer, Seven Lanterns, or Oriel Retreats ad styles
• Large, emotive imagery with elegant typography
• Clean layout that speaks luxury, clarity, and trust
Copy Direction (draft):
For those who’ve explored the world—and crave something beyond the ordinary.
Each journey is a masterfully curated experience, rich in detail, seamless in execution, and unforgettable in every way.
Founded in 1997, Tidewell Journeys is a unique travel company specializing in cruising, all-inclusive luxury properties, and tours world-wide for individuals, groups, and incentives.
We offer an exceptional range of services designed to ensure every journey is flawlessly executed and truly unforgettable.
Let us help you plan your next extraordinary adventure.
Note: You may refine the copy slightly based on layout or format needs.
Other Resources for References:
1. Website - www.tidewelljourneys.example

```html
<!DOCTYPE html>
<html lang="en">
<head>
<meta charset="utf-8">
<title>Tidewell Journeys – One-of-a-Kind Luxury Travel</title>
<link href="https://fonts.googleapis.com/css2?family=Cinzel:wght@600;700;800&family=Figtree:wght@400;500&display=swap" rel="stylesheet">
<style>
  :root {
    --backdrop: #cbc7c3;
    --ink: #231f20;
    --ink-soft: #2b2826;
    --white: #ffffff;
    --gold: #ddd27e;
    --rule: rgba(236, 214, 170, 0.75);
    --sky-top: #c3c7cc;
    --sky-low: #b9bcc0;
    --ridge: #6b4a34;
    --ridge-dark: #2a1d17;
    --dune-shadow: #3b2616;
    --dune: #c48f45;
    --dune-light: #d9ac63;
    --band-top: rgba(150, 104, 48, 0.92);
    --band-bottom: rgba(82, 58, 30, 0.97);
  }
  * { margin: 0; padding: 0; box-sizing: border-box; }
  html, body {
    width: 774px;
    height: 1200px;
    overflow: hidden;
    background: var(--backdrop);
  }
  .ad {
    position: absolute;
    left: 0;
    top: 99px;
    width: 774px;
    height: 1002px;
    overflow: hidden;
    font-family: "Figtree", Arial, sans-serif;
    color: var(--white);
  }
  .ad-photo {
    position: absolute;
    inset: 0;
    background:
      radial-gradient(ellipse 55% 30% at 72% 72%, var(--dune-light) 0%, rgba(217,172,99,0) 70%),
      radial-gradient(ellipse 40% 22% at 40% 68%, var(--dune-shadow) 0%, rgba(59,38,22,0) 75%),
      linear-gradient(to bottom,
        var(--sky-top) 0%,
        var(--sky-low) 26%,
        var(--ridge) 34%,
        var(--ridge-dark) 44%,
        #4a3222 54%,
        #8d6032 62%,
        var(--dune) 72%,
        #c99650 80%,
        #9a6b36 100%);
  }
  .info-band {
    position: absolute;
    left: 0;
    top: 760px;
    width: 774px;
    height: 242px;
    background: linear-gradient(to bottom, var(--band-top), var(--band-bottom));
  }
  .headline {
    position: absolute;
    left: 56px;
    top: 40px;
    font-family: "Cinzel", Georgia, serif;
    font-weight: 800;
    font-size: 66px;
    line-height: 60px;
    color: var(--ink);
    letter-spacing: -0.5px;
  }
  .subhead {
    position: absolute;
    left: 58px;
    top: 174px;
    width: 420px;
    font-size: 20.5px;
    line-height: 23px;
    color: var(--ink-soft);
  }
  .features {
    position: absolute;
    right: 50px;
    top: 346px;
    width: 380px;
    text-align: right;
  }
  .feature { margin-bottom: 18px; }
  .feature-title {
    font-family: "Cinzel", Georgia, serif;
    font-weight: 700;
    font-size: 20px;
    line-height: 24px;
    color: var(--gold);
  }
  .feature-text {
    font-size: 15.5px;
    line-height: 18.5px;
    color: var(--white);
  }
  .pitch {
    position: absolute;
    left: 58px;
    top: 535px;
    width: 380px;
  }
  .pitch-title {
    font-family: "Cinzel", Georgia, serif;
    font-weight: 700;
    font-size: 20px;
    line-height: 22px;
    color: var(--white);
  }
  .pitch-text {
    margin-top: 6px;
    font-size: 12.8px;
    line-height: 15px;
  }
  .about {
    position: absolute;
    left: 58px;
    top: 800px;
    width: 420px;
  }
  .about-title {
    font-family: "Cinzel", Georgia, serif;
    font-weight: 700;
    font-size: 23px;
    line-height: 26px;
  }
  .about p {
    font-size: 15.5px;
    line-height: 17.5px;
  }
  .about p + p { margin-top: 14px; }
  .divider {
    position: absolute;
    left: 493px;
    top: 794px;
    width: 1px;
    height: 176px;
    background: var(--rule);
  }
  .cta {
    position: absolute;
    left: 519px;
    top: 814px;
    width: 240px;
  }
  .cta-title {
    font-family: "Cinzel", Georgia, serif;
    font-weight: 700;
    font-size: 22px;
    line-height: 24.5px;
    color: var(--gold);
  }
  .cta-url {
    margin-top: 18px;
    font-family: "Cinzel", Georgia, serif;
    font-weight: 600;
    font-size: 11px;
    letter-spacing: 0;
    white-space: nowrap;
    color: var(--white);
    text-transform: uppercase;
  }
</style>
</head>
<body>
  <main class="ad">
    <div class="ad-photo" role="img" aria-label="Full-bleed photograph of rugged snow-dusted desert mountains at dusk above sweeping golden sand dunes"></div>
    <div class="info-band"></div>

    <h1 class="headline">One-of-a-kind<br>Luxury Travel</h1>
    <p class="subhead">Once-in-a-lifetime experiences that are curated with creativity and meticulous attention to detail</p>

    <section class="features">
      <div class="feature">
        <h2 class="feature-title">Exceptional Service:</h2>
        <p class="feature-text">White-glove, personalized planning<br>from start to finish</p>
      </div>
      <div class="feature">
        <h2 class="feature-title">38 Years’ Travel Experience:</h2>
        <p class="feature-text">expert knowledge of destinations, modes<br>of travel, premium accommodations and<br>well-established, meaningful industry<br>connections.</p>
      </div>
      <div class="feature">
        <h2 class="feature-title">Highly Trusted:</h2>
        <p class="feature-text">Cruise line executives often say,<br>“No one does what you do.”</p>
      </div>
    </section>

    <section class="pitch">
      <h2 class="pitch-title">For those who’ve<br>explored the world and<br>crave something<br>beyond the ordinary.</h2>
      <p class="pitch-text">Each journey is a masterfully curated<br>experience, rich in detail, seamless in execution,<br>and unforgettable in every way.</p>
    </section>

    <section class="about">
      <h2 class="about-title">Founded in 1997,</h2>
      <p>Tidewell Journeys is a unique travel company specializing in cruising, all-inclusive luxury properties, and tours world-wide for individuals, groups, and incentives.</p>
      <p>We offer an exceptional range of services designed to ensure every journey is flawlessly executed and truly unforgettable.</p>
    </section>

    <div class="divider"></div>

    <section class="cta">
      <h2 class="cta-title">Let us<br>help you plan<br>your next<br>extraordinary<br>adventure.</h2>
      <p class="cta-url">www.tidewelljourneys.example</p>
    </section>
  </main>
</body>
</html>
```